10-year customer thank you card

We want a greeting card that our sales reps can send to companies/customers who have been with our company for 10 or more years. We're a software company, our corporate color is blue but we also like green, orange, and purple. We'd like something rather minimal/simplistic for this card, perhaps building off our tree logo. We're really open to ideas for this one. You must use the template files that are uploaded. Copy included in 10 year thank you card file; the copy may change based on how it looks when laid out
Updates

I updated our brief. We'd prefer a sans serif font. I also uploaded a blank infographic image that includes more of our approved colors.

Industry/Entity Type

Software

Font styles to use
Sans Serif

```html
<!DOCTYPE html>
<html lang="en">
<head>
<meta charset="utf-8">
<title>10 Years — Thank You Card</title>
<link href="https://fonts.googleapis.com/css2?family=Cinzel:wght@400;500;700&display=swap" rel="stylesheet">
<style>
  :root {
    --sky: #5bc3f0;
    --coral: #ec6243;
    --white: #ffffff;
  }
  * { margin: 0; padding: 0; box-sizing: border-box; }
  html, body {
    width: 1200px;
    height: 851px;
    overflow: hidden;
    background: var(--sky);
  }
  .card {
    position: relative;
    width: 1200px;
    height: 851px;
    background: var(--sky);
    font-family: "Cinzel", serif;
  }
  .milestone {
    position: absolute;
    left: 0;
    right: 0;
    top: 190px;
    display: flex;
    flex-direction: column;
    align-items: center;
  }
  .milestone-number {
    display: flex;
    align-items: flex-end;
    color: var(--coral);
    font-weight: 400;
    font-size: 360px;
    line-height: 0.9;
    letter-spacing: -0.04em;
  }
  .milestone-zero {
    position: relative;
    display: inline-block;
  }
  .brand-name {
    position: absolute;
    left: 50%;
    top: 52%;
    transform: translate(-50%, -50%);
    color: var(--white);
    font-size: 20px;
    font-weight: 500;
    letter-spacing: 0.04em;
    line-height: 1;
  }
  .milestone-label {
    margin-top: -36px;
    color: var(--white);
    font-weight: 700;
    font-size: 86px;
    line-height: 1;
    letter-spacing: -0.01em;
  }
  .sign-off {
    position: absolute;
    left: 0;
    right: 0;
    top: 718px;
    height: 64px;
  }
  .sign-off-rule {
    position: absolute;
    left: 0;
    right: 0;
    top: 31px;
    height: 3px;
    background: var(--coral);
  }
  .sign-off-text {
    position: absolute;
    left: 50%;
    top: 0;
    transform: translateX(-50%);
    display: flex;
    align-items: center;
    gap: 12px;
    padding: 0 4px;
    background: var(--sky);
    height: 64px;
  }
  .brace {
    color: var(--coral);
    font-size: 60px;
    font-weight: 400;
    line-height: 1;
  }
  .thanks {
    color: var(--white);
    font-size: 40px;
    font-weight: 400;
    letter-spacing: 0.02em;
    line-height: 1;
  }
</style>
</head>
<body>
  <main class="card">
    <section class="milestone">
      <div class="milestone-number">
        <span class="milestone-one">1</span><span class="milestone-zero">0<span class="brand-name">Cedarline</span></span>
      </div>
      <div class="milestone-label">YEARS</div>
    </section>
    <footer class="sign-off">
      <div class="sign-off-rule"></div>
      <div class="sign-off-text">
        <span class="brace">{</span>
        <span class="thanks">Thank You</span>
        <span class="brace">}</span>
      </div>
    </footer>
  </main>
</body>
</html>
```